Cindermoor Larder Logo/Label Design

I am designing a blueberry label that will be placed on clam shells when the fruit is packed. The label will the company name "The Cindermoor Larder". It will also list Blueberries/Bleuets (Blueberries in French). It small print it would say Dist. By/Par The Cindermoor Larder, Lorne, ME 39724 USA. It would also list the package size. 1 US Dry Pint/1 Chopine Seche US 551 ml. I have provided some sample labels that other marketers use.

```html
<!DOCTYPE html>
<html lang="en">
<head>
<meta charset="utf-8">
<title>The Cindermoor Larder – Blueberries Label</title>
<link href="https://fonts.googleapis.com/css2?family=Fraunces:opsz,wght@144,900&family=Montserrat:wght@400;500&display=swap" rel="stylesheet">
<style>
  :root {
    --page-bg: #e6eafb;
    --navy: #0d1b5e;
    --navy-deep: #0a1550;
    --royal: #1d4fd8;
    --sky: #4a90e2;
    --sky-light: #6fd0f3;
    --mist: #dff4fd;
    --white: #ffffff;
    --brand-blue: #4fb3ef;
    --ink: #2b3a5c;
    --ink-soft: #5c7196;
    --berry: #3b5a86;
    --berry-dark: #1e3356;
  }
  * { margin: 0; padding: 0; box-sizing: border-box; }
  html, body {
    width: 1200px; height: 858px; overflow: hidden;
    background: var(--page-bg);
  }
  .label {
    position: absolute; left: 60px; top: 92px;
    width: 1080px; height: 675px;
    border-radius: 46px; overflow: hidden;
    background: var(--mist);
  }
  .label-waves { position: absolute; inset: 0; width: 100%; height: 100%; }
  .brand-name {
    position: absolute; left: 714px; top: 36px;
    transform: translateX(-50%);
    font-family: "Fraunces", Georgia, serif; font-weight: 900;
    font-size: 54px; line-height: 50px; letter-spacing: -1.5px;
    color: var(--brand-blue); text-align: center; white-space: nowrap;
  }
  .product-name {
    position: absolute; left: 398px; width: 644px;
    font-family: "Fraunces", Georgia, serif; font-weight: 900;
    color: var(--white); text-align: center; line-height: 1;
    font-size: 110px; letter-spacing: -1px;
  }
  .product-name--en { top: 220px; }
  .product-name--fr { top: 343px; }
  .name-divider {
    position: absolute; left: 421px; top: 335px;
    width: 637px; height: 5px; border-radius: 3px;
    background: rgba(255,255,255,0.35);
  }
  .fruit-photo {
    position: absolute; left: -20px; top: 225px;
    width: 450px; height: 390px;
    border-radius: 48% 52% 45% 50% / 50% 48% 52% 50%;
    background: radial-gradient(circle at 40% 40%, var(--berry) 0%, var(--berry-dark) 75%);
  }
  .net-content {
    position: absolute; left: 31px; top: 630px;
    font-family: "Montserrat", Arial, sans-serif; font-weight: 500;
    font-size: 23px; color: var(--ink-soft); white-space: nowrap;
  }
  .distributor {
    position: absolute; left: 808px; top: 592px;
    transform: translateX(-50%);
    font-family: "Montserrat", Arial, sans-serif; font-weight: 400;
    font-size: 26px; line-height: 28px; color: var(--ink);
    text-align: center; white-space: nowrap;
  }
</style>
</head>
<body>
  <main class="label">
    <svg class="label-waves" viewBox="0 0 1080 675" preserveAspectRatio="none" aria-hidden="true">
      <defs>
        <linearGradient id="mid-blue" x1="0" y1="0" x2="1" y2="0">
          <stop offset="0" stop-color="#6fd6f5"/>
          <stop offset="0.45" stop-color="#4a9de6"/>
          <stop offset="1" stop-color="#3f86dd"/>
        </linearGradient>
        <linearGradient id="bottom-mist" x1="0" y1="0" x2="0" y2="1">
          <stop offset="0" stop-color="#ffffff"/>
          <stop offset="1" stop-color="#c6ebfb"/>
        </linearGradient>
        <radialGradient id="navy-glow" cx="0.15" cy="0.2" r="0.6">
          <stop offset="0" stop-color="#1e3a8a"/>
          <stop offset="1" stop-color="#0a1550"/>
        </radialGradient>
      </defs>
      <rect width="1080" height="675" fill="url(#mid-blue)"/>
      <path d="M0 250 C 200 180, 420 200, 1080 290 L1080 0 L0 0 Z" fill="#3a7fe0" opacity="0.7"/>
      <path d="M0 215 C 220 150, 520 160, 1080 145 L1080 0 L0 0 Z" fill="#1f5ee0"/>
      <path d="M0 195 C 200 120, 480 140, 760 165 C 900 178, 1000 168, 1080 140 L1080 0 L0 0 Z" fill="url(#navy-glow)"/>
      <path d="M420 560 C 650 520, 880 500, 1080 450 L1080 675 L420 675 Z" fill="#8fdcf8"/>
      <path d="M380 580 C 640 560, 880 560, 1080 520 L1080 675 L380 675 Z" fill="#5ec8f6"/>
      <path d="M0 560 C 300 575, 700 600, 1080 570 L1080 675 L0 675 Z" fill="url(#bottom-mist)"/>
    </svg>

    <div class="fruit-photo" role="img" aria-label="Photo of ripe blueberries with green leaves"></div>

    <div class="brand-name">THE CINDERMOOR<br>LARDER</div>

    <h1 class="product-name product-name--en">Blueberries</h1>
    <div class="name-divider"></div>
    <p class="product-name product-name--fr" lang="fr">Bleuets</p>

    <p class="net-content">1 US Dry Pint / 1 Chopine Sèche US 551 ml</p>
    <p class="distributor">Dist. By / Par The Cindermoor Larder,<br>Lorne, ME 39724 USA</p>
  </main>
</body>
</html>
```